Two (Similar) Posters - Both 11" x 17"

We are looking for two posters - both 11" x 17" (vertical orientation) - to promote two consecutive, cardiology-related events:

Poster #1) The Inaugural New York RMC Quizline Competition, Cocktail Reception and Whiskey Tasting (http://brelvan-hsq.org/quizline-and-reception)

and

Poster #2) The 89th Annual Scientific Session and 27th Annual Meeting (http://brelvan-hsq.org/2017annualmtg)

#1 is a cocktail party with a whiskey tasting that will also feature a gameshow-like event with the med students, and #2 is an educational conference for doctors

Target Market(s)

Healthcare providers (Please do not include stock images of medical professionals; in fact, please use caution with any stock imagery, as it most likely will not be appropriate.)

Industry/Entity Type

Education

Colors

Designer to choose colors to be used in the design.

Requirements
Must have
• Each poster design should include:
• - the 4 logos of the participating organizations (I can upload various other versions if needed) along with the "wording" that goes alongside each one (see "STD_small" image as an example)
• - name of event
• - date, time and location
• - where to register
• - where to get more information
• - some artistic flavor or detailing
• Final (raw) files in an .ai, .psd, .eps or .idml format are required upon project completion.
Nice to have
• It's not crucial that these two posters "match," but it would be nice if they at least coordinated with each other. Would be nice if the designer could stay close to our color scheme (can be found here - http://brelvan-hsq.org/), but this isn't crucial. Posters should be upscale, neat and professional.
Should not have
• Should not be too difficult to read. These are posters that will likely be hanging on a bulletin board in hospital staff break rooms. Should not be too cartoon-like or silly. The two should not look EXACTLY the same in case people think that they are the same poster.

```html
<!DOCTYPE html>
<html lang="en">
<head>
<meta charset="utf-8">
<title>Event Posters</title>
<link rel="stylesheet" href="https://fonts.googleapis.com/css2?family=Cinzel:wght@400;700&display=swap">
<style>
:root{
  --navy:#0d2b5c;
  --gold:#c9a866;
  --gold-soft:#e4cf9f;
  --ink:#1d2a44;
  --strip:#dcdcdc;
  --page:#ece7de;
}
*{box-sizing:border-box;margin:0;padding:0}
html,body{width:1200px;height:1200px;overflow:hidden}
body{background:var(--page);font-family:'Cinzel',serif;color:var(--ink);position:relative}
.poster{position:absolute;top:230px;width:476px;height:738px;display:flex;flex-direction:column;box-shadow:0 4px 14px rgba(0,0,0,.25);background:var(--navy)}
.poster--reception{left:83px}
.poster--session{left:628px}
.hero{height:156px}
.hero--stage{background:linear-gradient(120deg,#3a2a6b 0%,#8a3c8c 30%,#2a1f3a 60%,#121018 100%)}
.hero--writing{background:linear-gradient(110deg,#8fb3d6 0%,#dfe7ee 45%,#f3f3f1 70%,#cfdce8 100%)}
.band{height:455px;padding:13px}
.frame{height:100%;border:4px solid var(--gold);background:#fff;padding:7px}
.panel{height:100%;border:1px solid var(--gold);display:flex;flex-direction:column}
.content{flex:1;background:linear-gradient(115deg,#f7f7f7 0%,#e9e9e9 40%,#fafafa 60%,#e6e6e6 100%);text-align:center;padding:18px 14px 8px;display:flex;flex-direction:column;align-items:center}
.title-top{font-size:16px;color:var(--navy);letter-spacing:.5px}
.title-main{font-size:19px;font-weight:700;color:var(--navy);margin-top:2px}
.session .title-top{font-size:16px}
.session .title-main{font-size:17px}
.presenter{font-size:6.5px;line-height:1.25;margin-top:6px;width:300px}
.flourish{width:180px;height:22px;margin:12px 0;background:linear-gradient(90deg,transparent,var(--gold-soft) 20%,var(--gold) 50%,var(--gold-soft) 80%,transparent);border-radius:11px;opacity:.85}
.line{font-size:10.5px;line-height:1.4;color:var(--navy)}
.line b{font-weight:700}
.rule{width:150px;height:1px;background:var(--gold);margin:6px 0}
.url{font-size:8px;font-weight:700;color:var(--navy);margin-top:8px;display:flex;align-items:center;gap:4px}
.small{font-size:9px;color:var(--navy);margin-top:6px;line-height:1.15}
.small .free{font-weight:700;font-size:11px}
.note{font-size:6.5px;color:var(--ink)}
.fee{font-size:10.5px;color:var(--navy);margin-top:4px}
.agenda{font-size:8px;line-height:1.3;color:var(--ink);margin-top:2px;width:270px}
.agenda p{margin-bottom:5px}
.agenda b{color:var(--navy);font-weight:700}
.agenda .gap{margin-top:9px}
.logos{height:64px;background:var(--strip);display:flex;align-items:center;justify-content:space-around;padding:0 6px}
.org{display:flex;align-items:center;gap:3px}
.org-mark{width:34px;height:34px;border-radius:50%;border:2px solid var(--navy);background:#fff;flex-shrink:0}
.org-name{font-size:5px;line-height:1.2;color:var(--navy);width:56px}
.gallery{height:127px;display:flex;gap:1px}
.shot{flex:1}
.shot--lounge{background:linear-gradient(160deg,#5a4a30,#2c2418 60%,#6b5a3e)}
.shot--dining{background:linear-gradient(160deg,#8a5a34,#3a2416 60%,#a06d3e)}
.shot--bar{background:linear-gradient(160deg,#6a4a34,#2a1c14 60%,#8a6a4a)}
.shot--counter{background:linear-gradient(160deg,#7c7a78,#2a2a2c 55%,#cfcfcf)}
.shot--ballroom{background:linear-gradient(160deg,#b08a58,#d6b78a 50%,#7a5a3a)}
</style>
</head>
<body>

<article class="poster poster--reception">
  <div class="hero hero--stage" role="img" aria-label="Audience applauding in front of a lit game show stage"></div>
  <div class="band">
    <div class="frame">
      <div class="panel">
        <div class="content">
          <h1 class="title-top">Cocktail Reception &amp;</h1>
          <h2 class="title-main">Inaugural RMC Quizline Event</h2>
          <p class="presenter">The event is presented by Brelvan Cardiological Society and the New York State Chapter of the Meridian College of Heart Science.</p>
          <div class="flourish" role="img" aria-label="Gold scroll ornament"></div>
          <p class="line">Wednesday, Dec. 6th, 2017</p>
          <p class="line"><b>Cocktails &amp; Networking:</b> 6:30 to 8:30 p.m.</p>
          <p class="line"><b>RMC Quizline Competition:</b> 8:30 to 9:30 p.m.</p>
          <p class="line"><b>Cash Bar:</b> 9:30 to 10:30 p.m.</p>
          <div class="rule"></div>
          <p class="line">Oak &amp; Ember, 14 E 41st St, New York, NY 10017</p>
          <div class="rule"></div>
          <p class="url"><svg width="8" height="8" viewBox="0 0 10 10"><circle cx="5" cy="5" r="4.5" fill="var(--navy)"/></svg>http://brelvan-hsq.org/quizline-and-reception</p>
          <p class="small">BHSQ/MCHS Member – <span class="free">Free</span><br><span class="note">(Limited space so first come, first served)</span></p>
          <p class="fee">BHSQ/MCHS Non-Members or Guests – $30/pp.</p>
          <div class="flourish" role="img" aria-label="Gold scroll ornament"></div>
        </div>
        <div class="logos">
          <div class="org"><span class="org-mark"></span><span class="org-name">Heart Exchange NY</span></div>
          <div class="org"><span class="org-mark"></span><span class="org-name">of the New York State Chapter Meridian College of Heart Science</span></div>
          <div class="org"><span class="org-mark"></span><span class="org-name">in association with Eastgate Cardiac Chapter</span></div>
          <div class="org"><span class="org-mark"></span><span class="org-name">presented by Brelvan Cardiological Society Inc</span></div>
        </div>
      </div>
    </div>
  </div>
  <div class="gallery">
    <div class="shot shot--lounge" role="img" aria-label="Lounge with fireplace and leather seating"></div>
    <div class="shot shot--dining" role="img" aria-label="Dining room with warm lighting"></div>
    <div class="shot shot--bar" role="img" aria-label="Bar area with bookshelves and fireplace"></div>
  </div>
</article>

<article class="poster poster--session session">
  <div class="hero hero--writing" role="img" aria-label="Hands writing notes with a pen at a desk"></div>
  <div class="band">
    <div class="frame">
      <div class="panel">
        <div class="content">
          <h1 class="title-top">The 89th Annual Scientific Session</h1>
          <h2 class="title-main">and 27th Annual Meeting</h2>
          <div class="flourish" role="img" aria-label="Gold scroll ornament"></div>
          <div class="agenda">
            <p><b>Cocktail Reception, Whiskey Tasting &amp; Inaugural New York RMC Quizline Competition:</b> Wednesday, Dec. 6th, 2017, from 6:30 to 10:30 p.m</p>
            <p><b>Scientific Session:</b> Thursday, Dec. 7th, 2017, from 7:30 a.m. to 3 p.m.</p>
            <p><b>Women in Cardiology (WIC) Networking Event:</b> Thursday, Dec. 7th, 2017, from 4:30 p.m. to 7 p.m.</p>
            <p><b>Council Meeting:</b> BHSQ Council Members Only</p>
            <p class="gap"><b>Cocktail Reception, Whiskey Tasting &amp; Inaugural NY RMC Quizline Competition:</b> Oak &amp; Ember, 14 E 41st St New York, NY</p>
            <p><b>Scientific Session:</b> The Harwell Ballroom, 22 E. 29th St., New York, NY</p>
            <p><b>Women in Cardiology (WIC) Networking Event:</b> Linwood's Park Avenue South, 412 Park Ave. South (at 28th Street)</p>
            <p><b>Council Meeting:</b> BHSQ Council Members Only</p>
          </div>
          <div class="flourish" role="img" aria-label="Gold scroll ornament"></div>
        </div>
        <div class="logos">
          <div class="org"><span class="org-mark"></span><span class="org-name">Heart Exchange NY</span></div>
          <div class="org"><span class="org-mark"></span><span class="org-name">of the New York State Chapter Meridian College of Heart Science</span></div>
          <div class="org"><span class="org-mark"></span><span class="org-name">in association with Eastgate Cardiac Chapter</span></div>
          <div class="org"><span class="org-mark"></span><span class="org-name">presented by Brelvan Cardiological Society Inc</span></div>
        </div>
      </div>
    </div>
  </div>
  <div class="gallery">
    <div class="shot shot--lounge" role="img" aria-label="Lounge with fireplace and leather seating"></div>
    <div class="shot shot--counter" role="img" aria-label="Modern bar counter with checkered floor"></div>
    <div class="shot shot--ballroom" role="img" aria-label="Ornate ballroom with gilded ceiling"></div>
  </div>
</article>

</body>
</html>
```